Geschäftspapier RVB
Zielgruppe
In den letzten Jahren konnten wir uns durch viel Engagement und Ehrgeiz zum Marktführer im Bereich Kaschierungen und Beschichtungen für den Automobilinnenraum in Europa entwickeln. Angeboten werden Rollenware sowie der Zuschnitt und die Weiterverarbeitung von kaschierten Verbundmaterialien und deren Entwicklung für den jeweiligen Einsatzzweck.
Die vielseitig hergestellten Verbundmaterialien aus Textil bis hin zu Kunst- und Echtledern findet man heute in vielen Bauteilen namhafter Automarken, der Flugzeug- und Schienenfahrzeugindustrie sowie in weiteren industriellen, technischen Anwendungen.
Beispiele dafür sind Innenverkleidungen und Sitze im Fahrzeug, Sonnenschutzkomponenten für den privaten und industriellen Bedarf, wie auch Bezüge von Kindersitzen oder medizinische Hygieneprodukte.
Aufgabenstellung
Zur Darstellung des Unternehmens wird ein neues Geschäftspapier gesucht. Dies sollte die folgenden Informationen zum Unternehmen, sowie die Bankkontakte enthalten. Ebenso sollte das vorhandene Firmenlogo integriert werden.
Das Unternehmen produziert hochwertige Textil-Produkte aus den Bereichen Automarken, der Flugzeug- und Schienenfahrzeugindustrie sowie in weiteren industriellen, technischen Anwendungen.
Das Geschäftspapier sollte diese Eigenschaft widerspiegeln und luxuriös, sowie modern erscheinen.
[Optional]
145 Jahre Erfahrung in der Textilveredlung - Führende Kaschier- und Beschichtungstechnologie
145 years of experience in textile processing - Leading technology in lamination and coating
Unternehmensfarbe Grün:
HKS 61 K
70% Cyan
0% Magenta
100% Gelb
75 % Schwarz
optionale Werbefarbe Anthrazit:
77% Cyan
72% Magenta
67% Gelb
84% Schwarz
Schriftart:
Arial

```html
<!DOCTYPE html>
<html lang="de">
<head>
<meta charset="utf-8">
<title>Geschäftspapier RVB</title>
<link href="https://fonts.googleapis.com/css2?family=Arimo:wght@400;700&display=swap" rel="stylesheet">
<style>
  :root{
    --green:#1d4d1a;
    --ink:#222;
    --paper:#fbfbfb;
    --backdrop:#ececee;
  }
  *{margin:0;padding:0;box-sizing:border-box}
  html,body{width:1200px;height:1200px;overflow:hidden;background:var(--backdrop)}
  body{font-family:"Arimo",Arial,sans-serif;color:var(--ink)}
  .sheet{position:absolute;left:190px;top:20px;width:820px;height:1160px;background:var(--green);padding:9px}
  .sheet-inner{position:relative;width:100%;height:100%;background:var(--paper);border-radius:22px}
  .brand{position:absolute;left:0;right:0;top:78px;text-align:center;font-size:64px;font-weight:400;color:var(--green);letter-spacing:6px}
  .fold-mark{position:absolute;left:0;width:21px;height:1px;background:#777}
  .sender-line{position:absolute;left:86px;top:203px;font-size:8px;white-space:nowrap}
  .sender-line b{font-weight:700}
  .recipient{position:absolute;left:86px;top:223px;font-size:13.5px;line-height:16.5px}
  .date-block{position:absolute;left:86px;top:335px;font-size:10.5px;line-height:13px}
  .label{color:var(--green);font-weight:700;font-size:11px}
  .subject{position:absolute;left:86px;top:383px;font-size:13.5px;font-weight:700}
  .letter-body{position:absolute;left:86px;top:446px;width:505px;font-size:13.5px;line-height:21px}
  .letter-body p{text-align:justify;hyphens:auto;margin-bottom:21px}
  .sidebar{position:absolute;left:626px;top:203px;width:175px;font-size:10.5px;line-height:13.5px}
  .sidebar .group{margin-bottom:9px}
  .banks{position:absolute;left:630px;top:775px;width:180px;font-size:10.5px;line-height:13.5px}
  .banks .bank{margin-bottom:9px}
  .banks .bank-name{font-weight:700;font-size:10.5px}
</style>
</head>
<body>
<div class="sheet">
  <div class="sheet-inner">
    <div class="brand">RVB</div>

    <div class="fold-mark" style="top:402px"></div>
    <div class="fold-mark" style="top:572px"></div>
    <div class="fold-mark" style="top:812px"></div>

    <div class="sender-line"><b>RVB GmbH</b> &nbsp;|&nbsp; Werkstraße 7 &nbsp;|&nbsp; D-08410 Grünhain</div>

    <address class="recipient" style="font-style:normal">
      Jonas Beispiel<br>Lindenallee 12<br>Feldheim 4570<br>Deutschland
    </address>

    <div class="date-block"><div class="label">Datum</div>6. Januar 2015</div>

    <div class="subject">Dies ist eine Betreffzeile</div>

    <div class="letter-body">
      <p style="margin-bottom:19px">Sehr geehrter Herr Beispiel,</p>
      <p>dies ist ein Typoblindtext. An ihm kann man sehen, ob alle Buchstaben da sind und wie sie aussehen. Manchmal benutzt man Worte wie Hamburgefonts, Rafgenduks oder Handgloves, um Schriften zu testen. Manchmal Sätze, die alle Buchstaben des Alphabets enthalten - man nennt diese Sätze »Pangrams«. Sehr bekannt ist dieser: The quick brown fox jumps over the lazy old dog.</p>
      <p>Oft werden in Typoblindtexte auch fremdsprachige Satzteile eingebaut (AVAW® and Tefox™ are testing aussi la Kerning), um die Wirkung in anderen Sprachen zu testen. In Lateinisch sieht zum Beispiel fast jede Schrift gut aus. Quod erat demonstrandum. Seit 1975 fehlen in den meisten Testtexten die Zahlen, weswegen nach TypoGb. 204 § ab dem Jahr 2034 Zahlen in 86 der Texte zur Pflicht werden. Nichteinhaltung wird mit bis zu 245 € oder 368 $ bestraft. Genauso wichtig in sind mittlerweile auch Âçcèñtë, die in neueren Schriften aber fast immer enthalten sind. Ein wichtiges aber schwierig zu integrierendes Feld sind OpenType-Funktionalitäten. Je nach Software und Voreinstellungen können eingebaute Kapitälchen, Kerning oder Ligaturen (sehr pfiffig) nicht richtig dargestellt werden. Dies ist ein Typoblindtext. An ihm kann man sehen, ob alle Buchstaben da sind und wie sie aussehen. Manchmal benutzt man Worte wie Hamburgefonts, Rafgenduks.</p>
      <p style="text-align:left">Mit freundlichen Grüßen<br>Martin Kessler</p>
    </div>

    <aside class="sidebar">
      <div class="group"><div class="label">RVB GmbH</div>Werkstraße 7<br>D-08410 Grünhain</div>
      <div class="group"><div class="label">Postanschrift</div>Postfach 2204<br>D-08420 Auenbach</div>
      <div class="group"><div class="label">Kontakt</div>Phone: +49 3700 5550 0<br>Fax: +49 3700 5550 199<br>Web: www.rvb-werk.de<br>E-Mail: post@rvb-werk.de</div>
      <div class="group"><div class="label">Handelsregister</div>HRB 5180 AG Auenbach<br>UStIDNr.: DE 000123456</div>
      <div class="group"><div class="label">Geschäftsführer</div>Martin Kessler</div>
      <div class="group"><div class="label">Prokura</div>Lena Kessler, Paul Ahrend</div>
    </aside>

    <aside class="banks">
      <div class="label">Bankverbindungen</div>
      <div class="bank"><div class="bank-name">Sparkasse Talland</div>IBAN: DE00 1000 0000 1111<br>0000 01<br>BIC: TALLDE81XXX</div>
      <div class="bank"><div class="bank-name">Handelsbank Auenbach</div>IBAN: DE00 2000 0000 2222<br>0000 02<br>BIC: HABADE82XXX</div>
      <div class="bank"><div class="bank-name">Landbank Grünhain</div>IBAN: DE00 3000 0000 3333<br>0000 03<br>BIC: LABKDE83XXX</div>
      <div class="bank"><div class="bank-name">Bürgerbank Feldheim</div>IBAN: DE00 4000 0000 4444<br>0000 04<br>BIC: BUBFDE84XXX</div>
      <div class="bank"><div class="bank-name">Nordhansa Bank</div>IBAN: DE00 5000 0000 5555<br>0000 05<br>BIC: NOHADE85XXX</div>
    </aside>
  </div>
</div>
</body>
</html>
```